Professional business cards for our auto wholesale dealership.

Target Market(s)

New and used cars sales managers and middle class to higher end private party buyers.

Industry/Entity Type

Automotive

Contact Information for Business Card

Bayline Premier Motors
Marcus T Holloway
Owner
(555) 417-3860
baypremmotors@mailbox-example.net
Dealer Lic # 48261

Logo Text

Bayline Premier Motors, Bay Prem Motors, BPM, etc

Font styles to use
Serif
Sans Serif

Colors

Designer to choose colors to be used in the design.

Requirements
Must have
• A professional, but not pretentious, look
Nice to have
• It might be nice to see "BPM" in a shape form i.e. circle, triangle, etc in the corner or background somehwere
Should not have
• bright "girly" colors

```html
<!DOCTYPE html>
<html lang="en">
<head>
<meta charset="utf-8">
<title>Bayline Premier Motors — Business Cards</title>
<link rel="stylesheet" href="https://fonts.googleapis.com/css2?family=Cinzel:wght@500&family=Open+Sans:wght@400;600&display=swap">
<style>
  :root {
    --canvas: #e7e5e3;
    --card-white: #ffffff;
    --brand-red: #b81e38;
    --ink: #4a4a4a;
    --ink-soft: #6b6b6b;
    --divider: #dcdcdc;
    --on-red: #f6eef0;
  }
  * { margin: 0; padding: 0; box-sizing: border-box; }
  html, body {
    width: 1200px; height: 900px; overflow: hidden;
    background: var(--canvas);
  }
  .sheet {
    position: relative; width: 1200px; height: 900px;
    display: flex; align-items: center; justify-content: center; gap: 50px;
  }
  .card {
    width: 525px; height: 300px; position: relative;
    box-shadow: 0 6px 18px rgba(0,0,0,0.18);
  }
  .card--front {
    background: var(--card-white);
    display: flex;
  }
  .card--back {
    background: var(--brand-red);
    display: flex; align-items: center; justify-content: center;
  }
  .brand {
    display: flex; flex-direction: column; align-items: center; gap: 14px;
  }
  .brand__circle {
    width: 74px; height: 74px; border-radius: 50%;
    border: 5px solid currentColor;
  }
  .brand__name {
    font-family: "Cinzel", serif; font-weight: 500;
    font-size: 24px; line-height: 1.15; letter-spacing: 1px;
    text-align: center; text-transform: uppercase;
  }
  .card--front .brand { color: var(--brand-red); }
  .card--back .brand { color: var(--on-red); }
  .card--back .brand__name { font-size: 28px; }

  .front__brand-area {
    width: 265px; display: flex; align-items: center; justify-content: center;
  }
  .front__details {
    flex: 1; border-left: 1px solid var(--divider);
    margin: 22px 0; padding: 20px 0 0 18px;
    font-family: "Open Sans", sans-serif; color: var(--ink);
  }
  .person__name {
    font-family: "Cinzel", serif; font-weight: 500;
    color: var(--brand-red); font-size: 17px; letter-spacing: 0.5px;
  }
  .person__role {
    font-size: 10.5px; text-transform: uppercase; color: var(--ink-soft);
    margin-top: 1px;
  }
  .contact { list-style: none; margin-top: 16px; }
  .contact__item {
    display: flex; align-items: center; gap: 6px;
    font-size: 10.5px; text-transform: uppercase; line-height: 1.55;
  }
  .contact__icon { width: 10px; height: 10px; fill: var(--brand-red); flex: none; }
  .licence {
    margin-top: 16px; font-size: 12.5px; font-weight: 600;
    text-transform: uppercase; color: var(--ink);
  }
  .licence__label { color: var(--brand-red); }
</style>
</head>
<body>
<main class="sheet">
  <section class="card card--front" aria-label="Business card front">
    <div class="front__brand-area">
      <div class="brand">
        <span class="brand__circle" aria-hidden="true"></span>
        <p class="brand__name">Bayline<br>Premier Motors</p>
      </div>
    </div>
    <div class="front__details">
      <p class="person__name">Marcus T Holloway</p>
      <p class="person__role">Owner</p>
      <ul class="contact">
        <li class="contact__item">
          <svg class="contact__icon" viewBox="0 0 24 24" aria-hidden="true"><path d="M6.6 10.8a15.1 15.1 0 0 0 6.6 6.6l2.2-2.2a1 1 0 0 1 1-.25 11.4 11.4 0 0 0 3.6.57 1 1 0 0 1 1 1V20a1 1 0 0 1-1 1A17 17 0 0 1 3 4a1 1 0 0 1 1-1h3.5a1 1 0 0 1 1 1c0 1.25.2 2.45.57 3.57a1 1 0 0 1-.25 1z"/></svg>
          (555) 417-3860
        </li>
        <li class="contact__item">
          <svg class="contact__icon" viewBox="0 0 24 24" aria-hidden="true"><path d="M2 5h20v14H2z M2 5l10 8 10-8" stroke="#fff" stroke-width="1.5"/></svg>
          baypremmotors@mailbox-example.net
        </li>
      </ul>
      <p class="licence"><span class="licence__label">Dealer Lic</span> # 48261</p>
    </div>
  </section>

  <section class="card card--back" aria-label="Business card back">
    <div class="brand">
      <span class="brand__circle" aria-hidden="true"></span>
      <p class="brand__name">Bayline<br>Premier Motors</p>
    </div>
  </section>
</main>
</body>
</html>
```